Auto electrical business that is mobile so we come to you so it doesn't matter if the car, 4wd, cara

We need a business card designed that will capture people's attention. We are based in Bathurst & we are a Mobile Auto Electrical business that works on cars, 4dw's, caravans, trucks, farming equipment through to mining equipment

```html
<!DOCTYPE html>
<html lang="en">
<head>
<meta charset="utf-8">
<title>Brock's Mobile Auto Electrical – Business Cards</title>
<link href="https://fonts.googleapis.com/css2?family=Arimo:wght@700&display=swap" rel="stylesheet">
<style>
  :root {
    --backdrop: #cbcbcb;
    --card: #ffffff;
    --brand-yellow: #f1c419;
    --ink: #1b1b1b;
    --photo-sky: #5d8fc9;
    --photo-glow: #d9a531;
    --photo-dark: #3b3526;
  }
  * { margin: 0; padding: 0; box-sizing: border-box; }
  html, body {
    width: 1200px; height: 1000px; overflow: hidden;
    background: var(--backdrop);
    font-family: "Arimo", Arial, sans-serif;
    font-weight: 700;
    color: var(--ink);
  }
  .card {
    position: absolute;
    background: var(--card);
    text-align: center;
  }
  .card--front { left: 355px; top: 170px; width: 490px; height: 301px; }
  .card--back  { left: 354px; top: 530px; width: 492px; height: 300px; }

  .photo-panel {
    position: absolute; left: 0; top: 0; width: 175px; height: 100%;
    background: linear-gradient(180deg, var(--photo-sky) 0%, #8a8fa0 35%, var(--photo-glow) 65%, var(--photo-dark) 100%);
  }
  .accent-stripe {
    position: absolute; left: 175px; top: 0; width: 6px; height: 100%;
    background: var(--brand-yellow);
  }
  .front-content {
    position: absolute; left: 181px; right: 0; top: 0; bottom: 0;
  }
  .brand-name {
    color: var(--brand-yellow);
    line-height: 1;
    letter-spacing: 0.5px;
  }
  .brand-tagline { line-height: 1; }

  .card--front .brand-name { font-size: 38px; margin-top: 32px; }
  .card--front .brand-tagline { font-size: 13px; margin-top: 2px; }
  .label { color: var(--brand-yellow); font-size: 18px; }
  .card--front .label--phone { margin-top: 48px; }
  .phone-lines { font-size: 22px; line-height: 24px; margin-top: 4px; }
  .card--front .label--email { margin-top: 36px; }
  .email { font-size: 16px; margin-top: 2px; }

  .card--back .brand-name { font-size: 54px; margin-top: 28px; }
  .card--back .brand-tagline { font-size: 18px; margin-top: 2px; }
  .services {
    font-size: 17.5px; line-height: 21px; letter-spacing: 1px;
    margin: 32px auto 0; width: 450px;
  }
  .card--back .label--phone { margin-top: 22px; }
  .phone-inline { font-size: 22px; margin-top: 2px; }
</style>
</head>
<body>
  <section class="card card--front">
    <div class="photo-panel" role="img" aria-label="Photo of an industrial plant structure lit up at dusk"></div>
    <div class="accent-stripe"></div>
    <div class="front-content">
      <div class="brand-name">Brock's</div>
      <div class="brand-tagline">Mobile Auto Electrical</div>
      <div class="label label--phone">Phone:</div>
      <div class="phone-lines">0491 57SPARK<br>0491 577275</div>
      <div class="label label--email">Email:</div>
      <div class="email">brocksmobile1@example.com</div>
    </div>
  </section>

  <section class="card card--back">
    <div class="brand-name">Brock's</div>
    <div class="brand-tagline">Mobile Auto Electrical</div>
    <p class="services">ALL FARMING AND PLANT EQUIPAMENT, AIR-CON NEEDS, LIGHT AND HEAVY VEHICLE, CARAVAN AND CAMPING SYSTEMS.</p>
    <div class="label label--phone">Phone</div>
    <div class="phone-inline">0491 57SPARK / 0491577275</div>
  </section>
</body>
</html>
```